Legal Agribusiness Capability Brochure Design

Design A4 sized 6 page Legal Agribusiness Capability Brochure. Design is to be consistent with current marketing materials - logo, letterhead, website and business card to be provided.
Cover page - Firm name and logo, Agribusiness Capability Statement heading with image 1 below
Inside cover page - About Us section with image 2 below then Awards section below image
Inside middle page - Our Expertise with image 3 below
Inside back page - Our Experience with image 4 below
Back page - Senior Lawyers with image 5 below
Outside Middle Back Page - Contact Us with image 6
Updates

To provide more details to designers for brochure

Target Market(s)

Agribusiness - Australia

Industry/Entity Type

Legal

Colors

Designer to choose colors to be used in the design.

Requirements
Must have
• Use content from uloaded file - Agribusiness Brochure Content
• Use images uploaded
• Professional appearance
• Consistent with current marketing and website https://tallowcreeklegal.com.au/

```html
<!DOCTYPE html>
<html lang="en">
<head>
<meta charset="utf-8">
<title>Tallow Creek Legal – Agribusiness Capability Statement</title>
<link href="https://fonts.googleapis.com/css2?family=Oswald:wght@500;600&family=Roboto:wght@400;500;700&family=Open+Sans:wght@400;600;700&display=swap" rel="stylesheet">
<style>
:root{
  --board:#b9b9c4;
  --blue:#1b84c9;
  --yellow:#e5c33f;
  --grey:#e4e4e8;
  --ink:#2a2a2a;
  --muted:#8a8a8a;
  --brown:#3a2e24;
  --white:#ffffff;
}
*{box-sizing:border-box;margin:0;padding:0}
html,body{width:1200px;height:3016px;overflow:hidden}
body{background:var(--board);font-family:"Open Sans",Arial,sans-serif;color:var(--ink);position:relative}
.page{position:absolute;background:var(--white);overflow:hidden;box-shadow:0 4px 10px rgba(0,0,0,.25)}
.abs{position:absolute}
.photo{position:absolute}

/* brand */
.brand{position:absolute;display:flex;align-items:center;gap:8px}
.seal,.award-badge{border-radius:50%;flex:none}
.seal{width:40px;height:40px;border:3px solid #444;background:#fff}
.award-badge{width:40px;height:40px;border:3px solid #d9c27a;background:#fbf6e4}
.brand-mark{width:30px;height:30px;background:var(--blue);flex:none}
.brand-text{display:flex;flex-direction:column;line-height:1}
.brand-name{font-family:"Roboto",Arial,sans-serif;font-weight:500;font-size:19px;color:var(--blue);letter-spacing:.3px}
.brand-tag{font-family:"Roboto",Arial,sans-serif;font-size:10px;color:#555;margin-top:3px}

/* cover */
.cover{left:368px;top:105px;width:452px;height:641px}
.cover-title{position:absolute;right:42px;top:140px;text-align:right;font-family:"Oswald",sans-serif;font-weight:600;color:#fff;font-size:31px;line-height:1.15;letter-spacing:.2px}
.cover-rule{position:absolute;left:120px;right:0;top:222px;height:3px;background:#fff}
.blue-foot{position:absolute;left:0;right:0;bottom:0;height:11px;background:var(--blue)}

/* spreads */
.spread{left:152px;width:916px;height:647px}
.spread-one{top:801px}
.spread-two{top:1503px}
.half{position:absolute;top:0;width:458px;height:100%}
.half.right{left:458px}
.tab{position:absolute;font-family:"Roboto",Arial,sans-serif;font-weight:700;font-size:15px;padding:4px 12px 3px;line-height:1.2}
.tab-blue-text{color:var(--blue);background:#fff}
.body-text{font-size:7.6px;line-height:1.28}
.body-text ul{list-style:none}
.body-text li::before{content:"• ";color:inherit}
.about-block{position:absolute;left:0;top:89px;width:458px;height:129px;background:var(--blue);color:#fff;padding:31px 18px 0}
.awards-box{position:absolute;left:29px;top:452px;width:401px;height:160px;background:#dededf;padding:26px 27px 0}
.awards-tab{position:absolute;left:141px;top:438px;width:164px;height:28px;background:#fff;border:2px solid var(--yellow);text-align:center;font-family:"Roboto",Arial,sans-serif;font-weight:500;color:var(--yellow);font-size:15px;line-height:24px}
.sub-head{color:var(--blue);font-weight:700;font-size:7.8px;margin-top:4px}
.expertise-block{position:absolute;left:0;top:89px;width:458px;height:269px;background:var(--grey);padding:32px 16px 0}
.expertise-block strong{font-weight:700}
.expertise-block li::before{color:var(--blue)}
.page-foot{position:absolute;left:0;right:0;top:622px;height:25px}
.foot-line{position:absolute;left:40px;right:40px;top:6px;height:2px;background:var(--blue)}
.page-no{position:absolute;top:0;width:46px;height:20px;background:var(--yellow);font-size:9px;line-height:20px;padding:0 10px;color:#333}
.page-no.left{left:0;border-radius:0 10px 10px 0}
.page-no.right{right:0;border-radius:10px 0 0 10px;text-align:right}

.experience-block{position:absolute;left:0;top:89px;width:458px;height:328px;background:var(--yellow);padding:32px 34px 0}
.experience-inner{position:absolute;left:12px;top:156px;width:427px;height:246px;border:2px solid #fff;padding:8px 12px 0}
.lawyer-photo{position:absolute;width:94px;height:94px;border-radius:50%;border:4px solid #fff;box-shadow:0 0 0 3px var(--blue)}
.lawyer-name{position:absolute;top:342px;border-left:3px solid var(--blue);padding-left:8px;font-family:"Roboto",Arial,sans-serif}
.lawyer-name b{display:block;font-size:15px;font-weight:700;color:#555}
.lawyer-name i{display:block;font-size:12px;color:#aaa;font-style:italic}
.bio{position:absolute;top:392px;font-size:7px;line-height:1.28;color:#444}
.bio ul{list-style:none}

/* back */
.back{left:371px;top:2221px;width:450px;height:636px}
.contact-panel{position:absolute;left:210px;top:115px;width:205px;height:512px;background:rgba(40,30,22,.93);color:#fff;padding:72px 16px 0}
.contact-title{font-family:"Oswald",sans-serif;font-weight:500;font-size:22px;margin-bottom:10px}
.contact-panel p{font-size:7.6px;line-height:1.35}
.office{margin-top:16px;font-size:7.6px;line-height:1.35}
.office b{display:block;font-weight:700}
.line{display:flex;gap:5px;align-items:flex-start}
.line svg{flex:none;margin-top:1px}
.web-btn{position:absolute;left:13px;bottom:30px;width:179px;height:24px;border-radius:12px;background:var(--yellow);color:var(--brown);font-weight:700;font-size:10px;text-align:center;line-height:24px}

.version{position:absolute;left:0;width:1200px;top:2912px;text-align:center;font-family:"Roboto",Arial,sans-serif;font-weight:700;font-size:36px;color:#fff}
</style>
</head>
<body>

<!-- Cover -->
<section class="page cover">
  <div class="photo" role="img" aria-label="Merino sheep standing in a line on dry red paddock under a pale sky" style="left:0;top:228px;width:452px;height:402px;background:linear-gradient(180deg,#d8c9b0 0%,#c2a888 40%,#9a6d4d 70%,#7c4e33 100%)"></div>
  <svg class="abs" style="left:0;top:0" width="452" height="300" viewBox="0 0 452 300">
    <polygon points="0,0 452,0 452,254 118,208 118,228 0,228" fill="var(--yellow)"/>
    <polygon points="118,208 452,254 452,262 118,216" fill="#2a2620"/>
    <polygon points="0,0 360,0 410,62 0,160" fill="#fff"/>
  </svg>
  <div class="brand" style="left:32px;top:18px">
    <span class="seal"></span>
    <span class="brand-mark"></span>
    <span class="brand-text"><span class="brand-name">TALLOW CREEK LEGAL</span><span class="brand-tag">Commercial + Litigation</span></span>
  </div>
  <div class="cover-title">AGRIBUSINESS<br>CAPABILITY STATEMENT</div>
  <div class="cover-rule"></div>
  <div class="blue-foot"></div>
</section>

<!-- Spread: pages 1–2 -->
<section class="page spread spread-one">
  <div class="half left">
    <div class="brand" style="left:66px;top:18px">
      <span class="seal"></span><span class="brand-mark"></span>
      <span class="brand-text"><span class="brand-name">TALLOW CREEK LEGAL</span><span class="brand-tag">Commercial + Litigation</span></span>
      <span class="award-badge"></span>
    </div>
    <div class="about-block body-text">
      <ul>
        <li>Independent commercial law firm with offices in Northam Bay and Kingsport</li>
        <li>Senior lawyers offering a combined 65 years of legal experience</li>
        <li>Practical advice in a professional and timely manner</li>
        <li>Client relationships built on trust</li>
        <li>Unfettered access to senior lawyers</li>
        <li>Direct and ongoing partner level involvement for each client</li>
        <li>Utilise the best information technology available to maintain high levels of efficiency and confidentiality</li>
      </ul>
    </div>
    <div class="tab" style="left:0;top:89px;background:#fff;color:var(--blue);border-radius:0 0 10px 0">ABOUT US</div>
    <div class="photo" role="img" aria-label="Rolling fields of yellow canola and green crops under a blue sky" style="left:0;top:218px;width:458px;height:254px;background:linear-gradient(180deg,#7fb0dc 0%,#b8d3e6 18%,#d9cf4a 35%,#6e8f3c 55%,#e8d12a 75%,#d9c21f 100%)"></div>
    <div class="awards-box body-text">
      <div class="sub-head">AGRIBUSINESS LEGAL AWARDS</div>
      <ul>
        <li>Ranked as a “Leading Agribusiness Law Firm – Western Australia, 2019” (Top 4)</li>
        <li>Ranked as a “Leading Agribusiness Law Firm – Western Australia, 2018” (Top 4)</li>
        <li>Ranked as a “Leading Agribusiness Law Firm – Western Australia, 2017” (Top 5)</li>
      </ul>
      <div class="sub-head" style="margin-top:9px">QUALITY PRACTICE STANDARD</div>
      <p>We are part of a select group of law firms which has been awarded the Quality Practice Standard by the State Law Society. As a result, we are able to better serve our clients by:</p>
      <ul>
        <li>Adopting modern quality management principles;</li>
        <li>Focusing on clients’ requirements and client care; and</li>
        <li>Striving for consistency of service for all clients by all at the firm.</li>
      </ul>
    </div>
    <div class="awards-tab">AWARDS</div>
  </div>
  <div class="half right">
    <div class="brand" style="left:58px;top:18px">
      <span class="seal"></span><span class="brand-mark"></span>
      <span class="brand-text"><span class="brand-name">TALLOW CREEK LEGAL</span><span class="brand-tag">Commercial + Litigation</span></span>
      <span class="award-badge"></span>
    </div>
    <div class="expertise-block body-text">
      <p>Over several decades our senior lawyers have advised clients involved in wheat, canola, lupin, wool, beef, dairy, wool, lamb, poultry, piggery, viticulture, forestry and plantation businesses. Our senior lawyers have strong family connections with pastoralists which allows them to better appreciate the challenges faced in agribusiness. Our family connection with pastoralists and our strong technical expertise in agribusiness law places Tallow Creek Legal in a unique position to advise clients in the agribusiness industry.</p>
      <p style="margin-top:8px"><strong>We can assist with the following agribusiness matters:</strong></p>
      <ul>
        <li>Agribusiness property contracts, agreements and deeds;</li>
        <li>Sale and purchase of agribusiness and farm assets;</li>
        <li>Pastoral lease advice;</li>
        <li>Native Title advice concerning access and compensation agreements;</li>
        <li>Land access agreements with mining, energy and telecommunications companies;</li>
        <li>Partnership, trust, corporation and joint venture advice;</li>
        <li>Farm Leases, Share Farming Agreements and Livestock Management Agreements;</li>
        <li>Carbon trading advice;</li>
        <li>Mortgages and securities;</li>
        <li>Farm succession planning, including Wills, Enduring Powers of Attorney and Guardianship;</li>
        <li>Employment advice;</li>
        <li>Deceased estates and probate, including advice concerning family provision claims; and</li>
        <li>Disputes.</li>
      </ul>
    </div>
    <div class="tab tab-blue-text" style="right:0;top:89px;border-radius:0 0 0 10px;background:#fff">EXPERTISE</div>
    <div class="photo" role="img" aria-label="Silhouette of a stockman on horseback mustering cattle in dust at sunset" style="left:0;top:358px;width:458px;height:254px;background:radial-gradient(circle at 72% 22%,#fff3d0 0%,#c9a66a 14%,#6b5334 40%,#2c2218 75%,#1a140e 100%)"></div>
  </div>
  <div class="page-foot">
    <div class="foot-line"></div>
    <div class="page-no left">p1</div>
    <div class="page-no right">p2</div>
  </div>
</section>

<!-- Spread: pages 3–4 -->
<section class="page spread spread-two">
  <div class="half left">
    <div class="brand" style="left:66px;top:18px">
      <span class="seal"></span><span class="brand-mark"></span>
      <span class="brand-text"><span class="brand-name">TALLOW CREEK LEGAL</span><span class="brand-tag">Commercial + Litigation</span></span>
      <span class="award-badge"></span>
    </div>
    <div class="experience-block body-text">
      <p><strong>Our senior lawyers have accumulated a wealth of experience in agribusiness law.</strong><br>Most of our work is subject to confidentiality which prevents us from disclosing any confidential information. However, we are able to disclose that our experience in agribusiness includes:</p>
    </div>
    <div class="tab" style="left:0;top:89px;background:#fff;color:var(--blue);border-radius:0 0 10px 0">EXPERIENCE</div>
    <div class="experience-inner body-text">
      <ul>
        <li>Advising clients with respect to the sale and acquisition of farmland, including due diligence enquiries, preparation and review of contracts for sale, registration of securities and settlement.</li>
        <li>Advising farmer in relation to the 180-megawatt Kellerton Wind Farm to be constructed on farmland near Marlow Flats, with a project value of up to AUD500 million and which is recognised as one of the best renewable projects in Australia.</li>
        <li>Advising pastoral lease holders on the sale and purchase of pastoral leases.</li>
        <li>Advising client on the termination of a vendor terms agreement for the sale of a farm and the repossession and resale of the farm.</li>
        <li>Advising numerous clients on various agreements with mining companies, including Royalty Agreements, Exploration Agreements, Land Access Deeds, Leases, Transmission Line Works Agreements, Deeds of Settlement and Release, Easement Deeds and Lay-Down Area Agreements.</li>
        <li>Advising on Access and Compensation Agreements with native title claimants.</li>
        <li>Advising client in relation to restructure of farmland and the transfer of the farmland to family members, trusts and a SMSF to qualify for the duties exemption under the Duties Act.</li>
        <li>Advising client in relation to the settlement of a farming partnership and trust dispute.</li>
        <li>Advising various farming families / corporate groups in relation to the restructuring of farm assets and exempt family farm transactions under the Duties Act.</li>
        <li>Advising farmers in relation to estate disputes and claims, including claims in the Supreme Court under the Family Provision Act.</li>
      </ul>
    </div>
    <div class="photo" role="img" aria-label="Outback windmill silhouetted against an orange sunset over red plains" style="left:0;top:417px;width:458px;height:195px;background:linear-gradient(180deg,#5f8fc4 0%,#b9a7b9 35%,#f0a24a 62%,#d4631f 75%,#8a3b1c 100%)"></div>
  </div>
  <div class="half right">
    <div class="brand" style="left:54px;top:18px">
      <span class="seal"></span><span class="brand-mark"></span>
      <span class="brand-text"><span class="brand-name">TALLOW CREEK LEGAL</span><span class="brand-tag">Commercial + Litigation</span></span>
      <span class="award-badge"></span>
    </div>
    <div class="photo" role="img" aria-label="Rows of autumn vineyard with a dirt track leading to the horizon" style="left:0;top:81px;width:458px;height:202px;background:linear-gradient(180deg,#7fb3e0 0%,#cfe0ec 20%,#9b4a3a 42%,#b98a4a 62%,#d5c3a4 100%)"></div>
    <div class="tab tab-blue-text" style="right:0;top:81px;border-radius:0 0 0 10px">SENIOR LAWYERS</div>
    <div class="lawyer-photo" role="img" aria-label="Portrait of Ben Carrow" style="left:81px;top:236px;background:linear-gradient(180deg,#e8e8ea,#9aa0aa)"></div>
    <div class="lawyer-photo" role="img" aria-label="Portrait of Alan Carrow" style="left:287px;top:236px;background:linear-gradient(180deg,#e8e8ea,#9aa0aa)"></div>
    <div class="lawyer-name" style="left:12px"><b>BEN CARROW</b><i>Principal</i></div>
    <div class="lawyer-name" style="left:240px"><b>ALAN CARROW</b><i>Consultant</i></div>
    <div class="bio" style="left:14px;width:214px">
      <p>Ben has practiced exclusively as a commercial lawyer for over 20 years initially at Kingsport law firms and since 2009 in Northam Bay. In 2011, Ben established Tallow Creek Legal in Northam Bay and expanded with the opening of a Kingsport office in 2017.<br>Ben has advised on a large number of commercial matters and disputes, particularly in relation to agribusiness, business, property, wills and estates.<br>He has a proven track record of delivering results to clients, especially in relation to more complex commercial transactions and disputes.<br>Ben has a specific interest in agribusiness, primarily due to his family being involved in agribusiness for several generations.</p>
      <p style="margin-top:8px">Ranked by Bramley’s Guide as a:</p>
      <ul>
        <li>• “Preeminent Agribusiness Lawyer – Western Australia, 2019” (Top 2 in W.A.)</li>
        <li>• “Leading Agribusiness Lawyer – Western Australia, 2018” (Top 5 in W.A.)</li>
        <li>• “Leading Agribusiness Lawyer – Western Australia, 2017” (Top 7 in W.A.)</li>
      </ul>
    </div>
    <div class="bio" style="left:242px;width:204px">
      <p>Alan was awarded a Bachelor of Laws from the State University in 1973. Since then Alan has been a partner at firms in Northam Bay and Port Ellery, as well as a principal of firms in Northam Bay and Port Ellery.<br>In late 2009 Alan and his wife, Ruth, made the decision to move back to Northam Bay where they had previously lived for approximately 11 years.<br>Alan has accumulated experience in a wide range of areas in over 45 years of legal practice, particularly in relation to Agribusiness disputes and litigation, which is of great benefit to his clients.</p>
    </div>
  </div>
  <div class="page-foot">
    <div class="foot-line"></div>
    <div class="page-no left">p3</div>
    <div class="page-no right">p4</div>
  </div>
</section>

<!-- Back page -->
<section class="page back">
  <div class="photo" role="img" aria-label="Yellow combine harvester working through a golden wheat crop" style="left:0;top:60px;width:450px;height:565px;background:linear-gradient(180deg,#5a4a32 0%,#8a6a3a 35%,#b48a44 60%,#c9a055 80%,#a97a35 100%)"></div>
  <svg class="abs" style="left:0;top:0" width="450" height="150" viewBox="0 0 450 150">
    <polygon points="0,0 450,0 450,70 0,142" fill="#fff"/>
  </svg>
  <div class="brand" style="left:72px;top:14px">
    <span class="seal"></span><span class="brand-mark"></span>
    <span class="brand-text"><span class="brand-name">TALLOW CREEK LEGAL</span><span class="brand-tag">Commercial + Litigation</span></span>
    <span class="award-badge"></span>
  </div>
  <div class="contact-panel">
    <div class="contact-title">CONTACT US</div>
    <p>If you have any questions or require any assistance in relation to agribusiness law, please contact us at our Northam Bay or Kingsport office.</p>
    <div class="office">
      <b>Northam Bay Office</b>
      <div class="line"><svg width="7" height="9" viewBox="0 0 7 9"><path d="M3.5 0a3.5 3.5 0 0 1 3.5 3.5C7 6 3.5 9 3.5 9S0 6 0 3.5A3.5 3.5 0 0 1 3.5 0z" fill="var(--yellow)"/></svg><span>Suite 2, Harbourside House<br>14 Jetty Lane<br>Northam Bay WA 6532</span></div>
      <div class="line"><svg width="7" height="8" viewBox="0 0 7 8"><path d="M1 0h2l1 2-1 1a5 5 0 0 0 2 2l1-1 1 1v2l-1 1C3 7 0 4 0 1z" fill="var(--yellow)"/></svg><span>+61 8 9000 4120</span></div>
      <div class="line"><svg width="7" height="8" viewBox="0 0 7 8"><rect x="0" y="3" width="7" height="4" fill="var(--yellow)"/><rect x="1.5" y="0" width="4" height="3" fill="var(--yellow)"/></svg><span>+ 61 8 9000 4121</span></div>
      <div class="line"><svg width="7" height="8" viewBox="0 0 7 8"><rect x=".5" y="2" width="6" height="4.5" fill="none" stroke="var(--yellow)"/><path d="M.5 2l3 2.5 3-2.5" fill="none" stroke="var(--yellow)"/></svg><span>info@tallowcreeklegal.com.au</span></div>
    </div>
    <div class="office">
      <b>Kingsport Office</b>
      <div class="line"><svg width="7" height="9" viewBox="0 0 7 9"><path d="M3.5 0a3.5 3.5 0 0 1 3.5 3.5C7 6 3.5 9 3.5 9S0 6 0 3.5A3.5 3.5 0 0 1 3.5 0z" fill="var(--yellow)"/></svg><span>62 Larkin Avenue<br>West Kingsport WA 6007</span></div>
      <div class="line"><svg width="7" height="8" viewBox="0 0 7 8"><path d="M1 0h2l1 2-1 1a5 5 0 0 0 2 2l1-1 1 1v2l-1 1C3 7 0 4 0 1z" fill="var(--yellow)"/></svg><span>+61 8 9000 5230</span></div>
      <div class="line"><svg width="7" height="8" viewBox="0 0 7 8"><rect x="0" y="3" width="7" height="4" fill="var(--yellow)"/><rect x="1.5" y="0" width="4" height="3" fill="var(--yellow)"/></svg><span>+ 61 8 9000 5231</span></div>
      <div class="line"><svg width="7" height="8" viewBox="0 0 7 8"><rect x=".5" y="2" width="6" height="4.5" fill="none" stroke="var(--yellow)"/><path d="M.5 2l3 2.5 3-2.5" fill="none" stroke="var(--yellow)"/></svg><span>info@tallowcreeklegal.com.au</span></div>
    </div>
    <div class="web-btn">www.tallowcreeklegal.com.au</div>
  </div>
  <div class="blue-foot"></div>
</section>

<div class="version">V1</div>

</body>
</html>
```